Meadowlark Soaps Business Card

The new business card design will incorporate my new logo components designed by one of your designers. Meadowlark Soaps creates high quality soaps and bath products. They would be suited for a Spa, Bed and Breakfast, Boutique environment. The look should be a white background.
Classy, soft and using the colour palet of the logo. The card will be two sided.

Reason: Need more time to make some changes and decide.

Target Market(s)

Looking to appeal to an upper end market. Spas, boutiques, independent gift stores, bridal salons, bed and breakfast, etc. I want the card to impart a sense of elegance, tranquility and Meadowlark. But also quality and value.

Industry/Entity Type

Business

Font styles to use
Sans Serif
Script

Requirements
Must have
• My logo on the front. But also on the back but faded out to allow written notes on the back.
On the front : Marta Quennell
Owner/Creator
47 Ashcombe Rd
Guelph, Ont K7R 2M5
555.014.2938
Creating Quality Handcrafted Soaps And Bath Products
Custom and Wholesale Orders Welcome
Www.meadowlarksoaps.ca
Www.friendline.net / MeadowlarkSoapandBath
info@meadowlarksoaps.ca

```html
<!DOCTYPE html>
<html lang="en">
<head>
<meta charset="utf-8">
<title>Meadowlark Soaps – Business Card</title>
<link rel="stylesheet" href="https://fonts.googleapis.com/css2?family=Open+Sans:wght@300;400;600&display=swap">
<style>
  :root {
    --page-bg: #ecebe8;
    --card-bg: #ffffff;
    --sage: #7ea69c;
    --sage-band: #8fb2a8;
    --sage-soft: #b9d0c9;
    --text-grey: #5f6361;
    --text-light: #8a8e8c;
    --shadow: rgba(40, 45, 43, 0.16);
  }
  html, body {
    margin: 0;
    padding: 0;
    width: 1200px;
    height: 892px;
    overflow: hidden;
    background: var(--page-bg);
    font-family: "Open Sans", Arial, sans-serif;
  }
  .canvas {
    position: relative;
    width: 1200px;
    height: 892px;
  }
  .card {
    position: absolute;
    top: 292px;
    width: 540px;
    height: 309px;
    background: var(--card-bg);
    box-shadow: 0 6px 22px var(--shadow);
    overflow: hidden;
  }
  .card--contact { left: 40px; }
  .card--brand { left: 620px; }

  /* Contact side */
  .contact-name {
    position: absolute;
    left: 44px;
    top: 34px;
    margin: 0;
    font-size: 21px;
    font-weight: 600;
    color: var(--sage);
  }
  .contact-role {
    position: absolute;
    left: 44px;
    top: 64px;
    margin: 0;
    font-size: 17px;
    font-weight: 400;
    color: var(--text-grey);
  }
  .contact-rule {
    position: absolute;
    left: 44px;
    top: 100px;
    width: 210px;
    height: 1px;
    background: var(--sage);
  }
  .contact-list {
    position: absolute;
    left: 44px;
    top: 116px;
    margin: 0;
    padding: 0;
    list-style: none;
    font-size: 11.5px;
    font-weight: 300;
    line-height: 20px;
    color: var(--text-grey);
  }
  .contact-list .label {
    font-weight: 600;
    color: var(--sage);
  }
  .tagline-band {
    position: absolute;
    left: 0;
    bottom: 0;
    width: 100%;
    height: 30px;
    background: var(--sage-band);
    color: #ffffff;
    font-size: 11.5px;
    font-weight: 300;
    line-height: 30px;
    text-align: center;
    letter-spacing: 0.2px;
  }

  /* Wordmark */
  .wordmark {
    position: absolute;
    display: flex;
    align-items: center;
    gap: 10px;
    color: var(--sage);
    font-weight: 400;
    white-space: nowrap;
  }
  .wordmark-dot {
    display: block;
    border-radius: 50%;
    background: var(--sage-soft);
  }
  .card--contact .wordmark {
    right: 34px;
    bottom: 62px;
    font-size: 22px;
  }
  .card--contact .wordmark-dot { width: 34px; height: 34px; }
  .card--brand .wordmark {
    left: 50%;
    top: 50%;
    transform: translate(-50%, -50%);
    font-size: 30px;
  }
  .card--brand .wordmark-dot { width: 46px; height: 46px; }

  /* Corner ornaments (placeholders) */
  .corner-ornament {
    position: absolute;
    width: 78px;
    height: 60px;
  }
  .corner-ornament--top { left: 14px; top: 14px; }
  .corner-ornament--bottom { right: 14px; bottom: 14px; }
</style>
</head>
<body>
<main class="canvas">

  <section class="card card--contact" aria-label="Card front with contact details">
    <h1 class="contact-name">Marta Quennell</h1>
    <p class="contact-role">Owner/Creator</p>
    <div class="contact-rule"></div>
    <ul class="contact-list">
      <li><span class="label">Phone:</span> 555.014.2938</li>
      <li>www.meadowlarksoaps.ca</li>
      <li>info@meadowlarksoaps.ca</li>
      <li>friendline.net / MeadowlarkSoapandBath</li>
      <li>47 Ashcombe Rd Guelph, Ont K7R 2M5</li>
    </ul>
    <div class="wordmark">
      <span class="wordmark-dot"></span>
      <span class="wordmark-name">Meadowlark Soaps</span>
    </div>
    <div class="tagline-band">Creating Quality Handcrafted Soaps And Bath Products. Custom and Wholesale Orders Welcome</div>
  </section>

  <section class="card card--brand" aria-label="Card back with brand name">
    <svg class="corner-ornament corner-ornament--top" role="img" aria-label="Flourish corner ornament in sage green" viewBox="0 0 78 60">
      <path d="M0 0 H78 V8 H8 V60 H0 Z" fill="var(--sage-soft)"/>
    </svg>
    <div class="wordmark">
      <span class="wordmark-dot"></span>
      <span class="wordmark-name">Meadowlark Soaps</span>
    </div>
    <svg class="corner-ornament corner-ornament--bottom" role="img" aria-label="Flourish corner ornament in sage green" viewBox="0 0 78 60">
      <path d="M78 60 H0 V52 H70 V0 H78 Z" fill="var(--sage-soft)"/>
    </svg>
  </section>

</main>
</body>
</html>
```